Business Card for my Photography/Video Business

I would like the card to say Event Photographer and Videographer. I like the Black and Gold look to it as well but open to other options. I don't want it to be super vibrant or colorful. Simple, elegant and professional

```html
<!DOCTYPE html>
<html lang="en">
<head>
<meta charset="UTF-8">
<title>LK Frames – Business Card</title>
<link rel="stylesheet" href="https://fonts.googleapis.com/css2?family=Montserrat:wght@500&family=Cormorant+Garamond:wght@500&family=Arimo&display=swap">
<style>
  :root {
    --backdrop: #2b2b2b;
    --card: #0b0b0b;
    --gold: #c9a646;
    --gold-soft: #b8953c;
  }
  html, body {
    margin: 0;
    width: 1200px;
    height: 997px;
    overflow: hidden;
    background: var(--backdrop);
  }
  .stage {
    position: relative;
    width: 1200px;
    height: 997px;
  }
  .card {
    position: absolute;
    left: 260px;
    width: 680px;
    height: 390px;
    background: var(--card);
    border-radius: 28px;
    box-shadow: 0 18px 40px rgba(0,0,0,0.45);
  }
  .card--front { top: 90px; }
  .card--back { top: 520px; }

  .brand {
    position: absolute;
    display: flex;
    align-items: center;
    gap: 26px;
  }
  .brand__dot {
    width: 118px;
    height: 118px;
    border-radius: 50%;
    background: var(--gold);
    flex: none;
  }
  .brand__name {
    font-family: "Montserrat", sans-serif;
    font-weight: 500;
    font-size: 64px;
    letter-spacing: 6px;
    color: var(--gold);
    line-height: 1;
  }
  .card--front .brand { left: 110px; top: 105px; }
  .tagline {
    position: absolute;
    left: 0;
    right: 0;
    top: 262px;
    text-align: center;
    font-family: "Cormorant Garamond", serif;
    font-weight: 500;
    font-size: 31px;
    letter-spacing: 1px;
    color: var(--gold-soft);
  }

  .card--back .brand { left: 110px; top: 80px; }
  .contact {
    position: absolute;
    left: 170px;
    top: 245px;
    font-family: "Arimo", sans-serif;
    font-size: 20px;
    color: var(--gold-soft);
    display: grid;
    grid-template-columns: auto auto;
    column-gap: 26px;
    row-gap: 12px;
  }
  .contact__item {
    display: flex;
    align-items: center;
    gap: 8px;
  }
  .contact__item--web { grid-column: 2; }
  .contact__icon {
    width: 14px;
    height: 14px;
    fill: var(--gold-soft);
  }
</style>
</head>
<body>
<main class="stage">
  <section class="card card--front">
    <div class="brand">
      <span class="brand__dot"></span>
      <span class="brand__name">LK FRAMES</span>
    </div>
    <p class="tagline">Event Photographer &amp; Videographer</p>
  </section>

  <section class="card card--back">
    <div class="brand">
      <span class="brand__dot"></span>
      <span class="brand__name">LK FRAMES</span>
    </div>
    <div class="contact">
      <span class="contact__item">
        <svg class="contact__icon" viewBox="0 0 16 16" aria-hidden="true"><path d="M2 5c0-2 2-3 3-3l1.5 3-1.5 1c.5 2 2.5 4 4.5 4.5l1-1.5 3 1.5c0 1-1 3-3 3C6 13.5 2.5 10 2 5z"/></svg>
        1300 555 019
      </span>
      <span class="contact__item">
        <svg class="contact__icon" viewBox="0 0 16 16" aria-hidden="true"><path d="M1 4h14v9H1z M1 4l7 5 7-5" fill="none" stroke="currentColor" stroke-width="0"/><path d="M1 4h14L8 9z"/><path d="M1 5.5l7 5 7-5V13H1z"/></svg>
        hello@lkframes.com
      </span>
      <span class="contact__item contact__item--web">
        <svg class="contact__icon" viewBox="0 0 16 16" aria-hidden="true"><circle cx="8" cy="8" r="6.5" fill="none" stroke="#b8953c" stroke-width="1.5"/><path d="M1.5 8h13M8 1.5c3 3 3 10 0 13M8 1.5c-3 3-3 10 0 13" fill="none" stroke="#b8953c" stroke-width="1.2"/></svg>
        www.lkframes.com
      </span>
    </div>
  </section>
</main>
</body>
</html>
```